Fun & Healthy Dog Treat Business Needs a Business & Loyalty Card

We need a business card design for a business that provides healthy dog products.

The design should communicate a healthy aspect and should communicate that the business focuses on healthy produce.

We would like some aspects if not all of our current logo to appear on the card.

We would also like a two sided card with the back of the card being able to be used as a loyalty program where after purchasing 7 items the buyer receives a free gift. There should be a way of identifying how many purchases a customer has made and if possible enable at least 4 - 5 gives be able to be given on one card. ie make 7 purchases and receive a give, to be able to be done 4 - 5 times before they need to be given a new card.

Rather than the focus be solely on dog treats we would like the card's focus to be a bit wider should we decide to enter other markets in the future and therefore not mention dog treats.

We want the card to be colourful while still retaining a very healthy aspect.

We also need the card to have pictures such as a dog or dogs head that enable us to determine how many items a customer has purchase before we give them a free gift.

Please see our website for further details regarding our business including contact details. www.wrenfieldpantry.com.au

Target Market(s)

Dog lovers who are health concious

Industry/Entity Type

Pet

Contact Information for Business Card

Products for Healthy Dogs
Web Address - www.wrenfieldpantry.com.au
Email address - info@wrenfieldpantry.com.au

Font styles to use
Serif

Colors
acd037
f04a50

Requirements
Must have
• Wrenfield Pantry
• Products for Healthy Dogs
• Web Address - www.wrenfieldpantry.com.au
• Email address - info@wrenfieldpantry.com.au
• Mobile Number - 0417 358 619
Nice to have
• Part of our current logo
• Blend in with current logo but not include the words healthy dog treats
• The flip side of the card should have a Loyalty Program where when you purchase 7 products you receive a free gift.
Should not have
• Should not include the words healthy dog treats
• Should not have the fixed line phone number

```html
<!DOCTYPE html>
<html lang="en">
<head>
<meta charset="utf-8">
<title>Wrenfield Pantry – Business &amp; Loyalty Cards</title>
<link href="https://fonts.googleapis.com/css2?family=Merriweather:wght@400;700;900&family=Open+Sans:wght@400;600;700&display=swap" rel="stylesheet">
<style>
  :root {
    --bg: #e9e9ea;
    --card: #ffffff;
    --red: #e01e2b;
    --red-dark: #c8121f;
    --green: #5cbf3a;
    --ink: #4a4a4a;
    --soft: rgba(0,0,0,.035);
  }
  * { box-sizing: border-box; margin: 0; padding: 0; }
  html, body { width: 1200px; height: 851px; overflow: hidden; }
  body {
    background: var(--bg);
    font-family: "Open Sans", Arial, sans-serif;
    position: relative;
  }
  .card {
    position: absolute;
    width: 520px;
    height: 300px;
    background: var(--card);
    border-radius: 18px;
    overflow: hidden;
    box-shadow: 0 10px 28px rgba(0,0,0,.18);
  }
  .brand {
    position: absolute;
    display: flex; align-items: center; gap: 10px;
    color: var(--red);
    font-family: "Merriweather", Georgia, serif;
    font-weight: 900;
    white-space: nowrap;
  }
  .brand-dot { border-radius: 50%; background: var(--green); flex: none; }
  .tagline {
    position: absolute;
    font-family: "Merriweather", Georgia, serif;
    font-size: 13px;
    color: var(--green);
    font-weight: 700;
    white-space: nowrap;
  }

  /* Loyalty side */
  .loyalty { left: 90px; top: 110px; }
  .paw-pattern {
    position: absolute; inset: 0;
    background: radial-gradient(ellipse at 50% 50%, transparent 40%, var(--soft) 100%);
  }
  .loyalty .brand { left: 110px; top: 50px; font-size: 30px; }
  .loyalty .brand-dot { width: 32px; height: 32px; }
  .loyalty .tagline { left: 152px; top: 100px; }
  .stamps {
    position: absolute; left: 34px; top: 162px;
    display: flex; gap: 20px;
  }
  .stamp { width: 46px; height: 40px; }
  .offer {
    position: absolute; left: 34px; top: 228px;
    font-size: 17px; color: var(--ink);
  }
  .offer .gift { color: var(--red); }

  /* Contact side */
  .contact { left: 590px; top: 430px; }
  .contact .bands { position: absolute; inset: 0; }
  .person {
    position: absolute; right: 28px; top: 20px;
    color: #fff; text-align: right;
  }
  .person-name { font-size: 19px; font-weight: 600; }
  .person-role { font-size: 13px; }
  .contact .brand { left: 60px; top: 146px; font-size: 27px; }
  .contact .brand-dot { width: 28px; height: 28px; }
  .contact .tagline { left: 98px; top: 190px; font-size: 12px; }
  .details {
    position: absolute; left: 98px; top: 218px;
    list-style: none; font-size: 13px; color: var(--ink);
  }
  .details li { display: flex; align-items: center; gap: 8px; height: 21px; }
  .details svg { width: 13px; height: 13px; flex: none; }
  .paws {
    position: absolute; right: 30px; top: 104px;
    width: 100px; height: 44px;
    background: radial-gradient(ellipse at 60% 50%, rgba(0,0,0,.07), transparent 70%);
  }
</style>
</head>
<body>

<section class="card loyalty" aria-label="Loyalty card">
  <div class="paw-pattern" role="img" aria-label="Faint paw print pattern across the card"></div>
  <div class="brand"><span class="brand-dot"></span>Wrenfield Pantry</div>
  <p class="tagline">Products for Healthy Dogs</p>
  <div class="stamps">
    <svg class="stamp" viewBox="0 0 46 40"><path d="M5 36 V18 C5 8 13 4 23 4 C33 4 41 8 41 18 V36 Z" fill="none" stroke="var(--red)" stroke-width="4" stroke-linejoin="round"/></svg>
    <svg class="stamp" viewBox="0 0 46 40"><path d="M5 36 V18 C5 8 13 4 23 4 C33 4 41 8 41 18 V36 Z" fill="none" stroke="var(--red)" stroke-width="4" stroke-linejoin="round"/></svg>
    <svg class="stamp" viewBox="0 0 46 40"><path d="M5 36 V18 C5 8 13 4 23 4 C33 4 41 8 41 18 V36 Z" fill="none" stroke="var(--red)" stroke-width="4" stroke-linejoin="round"/></svg>
    <svg class="stamp" viewBox="0 0 46 40"><path d="M5 36 V18 C5 8 13 4 23 4 C33 4 41 8 41 18 V36 Z" fill="none" stroke="var(--red)" stroke-width="4" stroke-linejoin="round"/></svg>
    <svg class="stamp" viewBox="0 0 46 40"><path d="M5 36 V18 C5 8 13 4 23 4 C33 4 41 8 41 18 V36 Z" fill="none" stroke="var(--red)" stroke-width="4" stroke-linejoin="round"/></svg>
    <svg class="stamp" viewBox="0 0 46 40"><path d="M5 36 V18 C5 8 13 4 23 4 C33 4 41 8 41 18 V36 Z" fill="none" stroke="var(--red)" stroke-width="4" stroke-linejoin="round"/></svg>
    <svg class="stamp" viewBox="0 0 46 40"><path d="M5 36 V18 C5 8 13 4 23 4 C33 4 41 8 41 18 V36 Z" fill="none" stroke="var(--red)" stroke-width="4" stroke-linejoin="round"/></svg>
  </div>
  <p class="offer">when you purchase 7 products you receive a <span class="gift">free gift.</span></p>
</section>

<section class="card contact" aria-label="Business card">
  <svg class="bands" viewBox="0 0 520 300" preserveAspectRatio="none">
    <defs>
      <linearGradient id="redBand" x1="0" y1="0" x2="1" y2="1">
        <stop offset="0" stop-color="var(--red-dark)"/>
        <stop offset="1" stop-color="var(--red)"/>
      </linearGradient>
    </defs>
    <path d="M0 0 H520 V72 C380 66 160 88 0 152 Z" fill="url(#redBand)"/>
    <path d="M0 164 C160 104 380 80 520 82 V90 C380 90 160 114 0 174 Z" fill="var(--green)"/>
  </svg>
  <div class="person">
    <div class="person-name">Nora Whitlock</div>
    <div class="person-role">CEO/Founder</div>
  </div>
  <div class="paws" role="img" aria-label="Small grey paw prints"></div>
  <div class="brand"><span class="brand-dot"></span>Wrenfield Pantry</div>
  <p class="tagline">Products for Healthy Dogs</p>
  <ul class="details">
    <li><svg viewBox="0 0 13 13"><rect x="3" y="0.8" width="7" height="11.4" rx="1.5" fill="none" stroke="var(--red)" stroke-width="1.6"/></svg>0417 358 619</li>
    <li><svg viewBox="0 0 13 13"><rect x="0.8" y="2.5" width="11.4" height="8" fill="var(--red)"/><path d="M1 3 L6.5 7.5 L12 3" fill="none" stroke="#fff" stroke-width="1.2"/></svg>info@wrenfieldpantry.com.au</li>
    <li><svg viewBox="0 0 13 13"><circle cx="6.5" cy="6.5" r="6" fill="var(--red)"/><path d="M1 6.5 H12 M6.5 0.5 C3.5 4 3.5 9 6.5 12.5 M6.5 0.5 C9.5 4 9.5 9 6.5 12.5" fill="none" stroke="#fff" stroke-width=".9"/></svg>www.wrenfieldpantry.com.au</li>
  </ul>
</section>

</body>
</html>
```